Modern Business Card for Industrial Company

We need business cards updated with modern fonts and make it look more technical, sharp and clean. The logo should not be changed, but we are looking for fresh solutions for how other information on the card is laid out in an interesting way. The company provides machinery and services to the ceramic industry and deals with cutting-edge technology. The design should reflect a technologically advanced and modern company that deals with the latest European technologies.

Font styles to use
Sans Serif

Requirements
Must have
• Modern fonts, technical look and feel

```html
<!DOCTYPE html>
<html lang="en">
<head>
<meta charset="utf-8">
<title>Novaro Service – Business Card</title>
<link rel="stylesheet" href="https://fonts.googleapis.com/css2?family=Jost:wght@400;500;600&family=Michroma&display=swap">
<style>
  :root {
    --stage: #cccccc;
    --card-light: #efefef;
    --card-dark: #1b1b1d;
    --brand-blue: #0a4f8f;
    --accent-red: #b8252b;
    --text-light: #ffffff;
    --pattern-light: rgba(190, 190, 190, 0.35);
    --pattern-dark: rgba(30, 60, 140, 0.35);
  }
  * { margin: 0; padding: 0; box-sizing: border-box; }
  html, body { width: 1033px; height: 1200px; overflow: hidden; }
  body { background: var(--stage); position: relative; font-family: 'Jost', sans-serif; }

  .card {
    position: absolute; left: 122px; width: 790px; height: 451px; overflow: hidden;
    box-shadow: 0 4px 18px rgba(0,0,0,0.12);
  }
  .card--front { top: 100px; background: var(--card-light); }
  .card--back { top: 649px; background: var(--card-dark); }

  .card__pattern { position: absolute; inset: 0; }
  .card--front .card__pattern {
    background: linear-gradient(135deg, transparent 10%, var(--pattern-light) 45%, transparent 80%);
  }
  .card--back .card__pattern {
    background: linear-gradient(135deg, transparent 5%, var(--pattern-dark) 40%, transparent 60%, var(--pattern-dark) 85%);
  }

  .brand-name {
    position: absolute; color: var(--brand-blue); font-weight: 600;
    text-align: center; line-height: 1; letter-spacing: 0.04em;
  }
  .card--front .brand-name { left: 0; right: 0; top: 110px; font-size: 96px; }
  .card--front .brand-name span { display: block; font-size: 56px; letter-spacing: 0.2em; margin-top: 14px; }
  .card--back .brand-name { left: 96px; width: 190px; top: 258px; font-size: 50px; }
  .card--back .brand-name span { display: block; font-size: 28px; letter-spacing: 0.14em; margin-top: 8px; }

  .website {
    position: absolute; color: var(--brand-blue); font-weight: 600; text-align: center; letter-spacing: 0.02em;
  }
  .card--front .website { left: 0; right: 0; top: 349px; font-size: 22px; }
  .card--back .website { left: 90px; width: 200px; top: 384px; font-size: 11px; font-weight: 500; }

  .person__name {
    position: absolute; left: 417px; top: 90px; color: var(--text-light);
    font-family: 'Michroma', sans-serif; font-size: 26px; line-height: 37px; letter-spacing: 0.02em;
  }
  .person__role {
    position: absolute; left: 497px; top: 164px; color: var(--text-light); font-size: 20px; letter-spacing: 0.03em;
  }
  .divider { position: absolute; left: 0; top: 0; }

  .contact { position: absolute; left: 390px; top: 232px; list-style: none; color: var(--text-light); font-size: 16px; line-height: 24px; }
  .contact li { display: flex; align-items: flex-start; gap: 10px; margin-bottom: 26px; }
  .contact li:nth-child(2) { margin-bottom: 26px; }
  .contact svg { flex: none; margin-top: 4px; }
</style>
</head>
<body>

<section class="card card--front">
  <div class="card__pattern" role="img" aria-label="Faint grey fine-line geometric pattern"></div>
  <div class="brand-name">NOVARO<span>SERVICE</span></div>
  <div class="website">WWW.NOVAROTECH.COM</div>
</section>

<section class="card card--back">
  <div class="card__pattern" role="img" aria-label="Dark blue fine-line geometric pattern"></div>

  <svg class="divider" width="790" height="200" viewBox="0 0 790 200" aria-hidden="true">
    <g stroke="var(--accent-red)" stroke-width="4" fill="none">
      <line x1="0" y1="153" x2="393" y2="153"/>
      <line x1="619" y1="153" x2="790" y2="153"/>
      <polyline points="340,153 362,177 474,177"/>
      <circle cx="480" cy="177" r="6" stroke-width="3"/>
    </g>
  </svg>

  <div class="person__name">MARCO<br>FERRETTI</div>
  <div class="person__role">President</div>

  <div class="brand-name">NOVARO<span>SERVICE</span></div>
  <div class="website">WWW.NOVAROTECH.COM</div>

  <ul class="contact">
    <li>
      <svg width="20" height="18" viewBox="0 0 20 18" aria-hidden="true"><path d="M10 0a6 6 0 0 0-6 6c0 4.5 6 12 6 12s6-7.5 6-12a6 6 0 0 0-6-6zm0 8.3a2.3 2.3 0 1 1 0-4.6 2.3 2.3 0 0 1 0 4.6z" fill="var(--accent-red)"/></svg>
      <span>418 halden road, suite 200<br>Marlow, ga 30117</span>
    </li>
    <li>
      <svg width="20" height="16" viewBox="0 0 20 16" aria-hidden="true"><path d="M1 1h18v14H1z" fill="var(--accent-red)"/><path d="M1 2l9 7 9-7" stroke="var(--card-dark)" stroke-width="1.6" fill="none"/></svg>
      <span>mferretti@novarotech.com</span>
    </li>
    <li>
      <svg width="20" height="16" viewBox="0 0 20 16" aria-hidden="true"><path d="M5 1l3 4-2 2c1 2 3 4 5 5l2-2 4 3-2 3C9 16 2 9 2 3z" fill="var(--accent-red)"/></svg>
      <span>555 014-2290</span>
    </li>
  </ul>
</section>

</body>
</html>
```